Mortgage Lender needs Flyers Designed

We are a wholesale mortgage lender providing mortgage services throughout the United States to mortgage brokers. We just merged with a company and need to redesign their product flyers and matrices so they are more in line with a modern and sleek look. We provide residential and commercial mortgage financing options. I have attached a document labeled TIDE BINDER. This is the current flyer set that needs to be redesigned for my company. There are 10 programs featured in the document. The first two pages provide a product overview and the following 17 pages are the matrices for each product. I need a design set created in either Adobe Photoshop or Adobe Indesign so we can edit the content as necessary.

Target Market(s)

Mortgage Brokers in the United States

Industry/Entity Type

Finance, Mortgage

Font styles to use
Serif
Sans Serif

Requirements
Must have
• Must include all ten programs and must be designed using Adobe Photoshop or Adobe InDesign (preferred)
Nice to have
• Great graphics and clean modern feel.
Should not have
• Typos, hard to edit fields, should not look very similar to the TIDE BINDER pdf attached.

```html
<!DOCTYPE html>
<html lang="en">
<head>
<meta charset="utf-8">
<title>Small-Balance Commercial Loans</title>
<link href="https://fonts.googleapis.com/css2?family=Merriweather:wght@700;900&family=Inter:wght@400;500;600&display=swap" rel="stylesheet">
<style>
  :root {
    --green: #45652f;
    --ink: #111111;
    --text: #2a2a2a;
    --red: #e0262a;
    --rule: #6f7f66;
    --grey-band: #e2e2e2;
    --paper: #ffffff;
  }
  * { margin: 0; padding: 0; box-sizing: border-box; }
  html, body { width: 848px; height: 1200px; overflow: hidden; background: var(--paper); }
  body { position: relative; font-family: "Inter", sans-serif; color: var(--text); }
  .abs { position: absolute; }

  .title { left: 57px; top: 46px; font-family: "Merriweather", serif; font-weight: 900; font-size: 40px; line-height: 46px; color: var(--ink); letter-spacing: -0.3px; }
  .title-rule { left: 0; top: 160.5px; width: 483px; height: 1.5px; background: var(--ink); }
  .title-pill { left: 57px; top: 156px; width: 86px; height: 10px; border-radius: 5px; background: var(--green); }

  .brand { left: 618px; top: 80px; width: 178px; text-align: center; }
  .brand-mark { width: 46px; height: 46px; border-radius: 50%; background: var(--green); margin: 0 auto 14px; }
  .brand-name { font-family: "Merriweather", serif; font-weight: 700; font-size: 17px; color: var(--ink); letter-spacing: 0.3px; border-bottom: 1.5px solid var(--ink); padding-bottom: 2px; white-space: nowrap; }
  .brand-url { font-family: "Inter", sans-serif; font-weight: 600; font-size: 7.5px; letter-spacing: 3px; margin-top: 5px; color: var(--ink); }

  .intro-card { left: 57px; top: 188px; width: 356px; height: 252px; border: 1.2px dashed var(--rule); border-top: none; border-right: none; border-radius: 0 0 0 6px; }
  .intro-head { left: 57px; top: 188px; width: 225px; height: 75px; background: var(--green); border-radius: 5px 0 0 0; color: #fff; font-family: "Merriweather", serif; font-weight: 700; font-size: 24.5px; line-height: 29px; padding: 8px 12px; }
  .intro-photo { left: 282px; top: 188px; width: 131px; height: 252px; border-radius: 0 8px 0 0; background: linear-gradient(160deg, #e6ebf3 0%, #c7d0de 35%, #9fa9ba 70%, #7e8794 100%); }
  .intro-body { left: 68px; top: 279px; width: 205px; font-size: 9.6px; line-height: 11.5px; color: var(--ink); }
  .intro-body p { text-align: justify; }
  .intro-body ul { list-style: none; margin-top: 12px; }
  .intro-body li { margin-bottom: 7px; }

  .section-title { font-family: "Merriweather", serif; font-weight: 700; font-size: 25px; color: var(--green); }

  .spec { position: absolute; font-size: 11.6px; font-weight: 600; color: var(--ink); padding-left: 16px; line-height: 14px; }
  .spec::before { content: ""; position: absolute; left: 0; top: 3px; border-left: 4px solid var(--ink); border-top: 3px solid transparent; border-bottom: 3px solid transparent; }
  .val { position: absolute; font-size: 9.6px; line-height: 11.5px; color: var(--ink); }

  .matrix { left: 58px; top: 650px; width: 742px; height: 475px; display: grid; grid-template-columns: 112px 169px 187px 150px 124px; grid-template-rows: 31px 222px 222px; }
  .matrix-frame { left: 58px; top: 650px; width: 742px; height: 475px; border: 1.2px dashed var(--rule); border-top: none; border-radius: 0 0 10px 10px; pointer-events: none; }
  .mh { background: var(--green); color: #fff; font-weight: 600; font-size: 14px; display: flex; align-items: center; justify-content: center; }
  .mh:first-child { border-radius: 12px 0 0 0; }
  .mh:last-child { border-radius: 0 12px 0 0; }
  .cell { border-left: 1px solid var(--rule); border-bottom: 1px solid var(--rule); padding: 7px 7px 6px 8px; font-size: 10.2px; line-height: 16px; color: var(--text); overflow: hidden; display: flex; flex-direction: column; }
  .cell.row-label { border-left: none; align-items: center; justify-content: center; text-align: center; font-weight: 600; font-size: 14px; line-height: 17px; color: var(--ink); }
  .row-label.left { align-items: flex-start; padding-left: 10px; }
  .last-row { border-bottom: none; }
  .yes { color: var(--green); line-height: 17px; }
  .no { color: var(--red); line-height: 17px; }
  .desc { line-height: 13px; margin-top: 3px; }
  .docs-block { margin-top: 9px; }
  .push .docs-block { margin-top: auto; }
  .docs-title { font-weight: 600; color: var(--ink); }
  .docs { list-style: none; padding-left: 11px; }
  .docs li { white-space: nowrap; }
  .docs li::before { content: "• "; }
  .docs li .cont { padding-left: 9px; display: block; }

  .footer-band { left: 0; top: 1128px; width: 848px; height: 72px; }
  .footer-url { left: 0; top: 1172px; width: 848px; text-align: center; font-family: "Merriweather", serif; font-weight: 700; font-size: 18px; letter-spacing: 7px; color: var(--ink); }
</style>
</head>
<body>

  <h1 class="abs title">Small-Balance<br>Commercial Loans</h1>
  <div class="abs title-rule"></div>
  <div class="abs title-pill"></div>

  <div class="abs brand">
    <div class="brand-mark"></div>
    <div class="brand-name">NORTHLINE CAPITAL</div>
    <div class="brand-url">NLCAPITAL.COM</div>
  </div>

  <div class="abs intro-card"></div>
  <div class="abs intro-head">This is lending done differently</div>
  <div class="abs intro-photo" role="img" aria-label="Photo of a light industrial warehouse with glass roll-up doors under a pale sky"></div>
  <div class="abs intro-body">
    <p>Let our experts help you secure flexible commercial mortgage financing on loans from $100K to $2MM.</p>
    <ul>
      <li>• No tax returns required</li>
      <li>• Flexible cash-outs</li>
      <li>• Wide range of eligible real estate</li>
      <li>• Broker-friendly compensation<br>(no lender points charged, YSP available)</li>
    </ul>
  </div>

  <h2 class="abs section-title" style="left:452px; top:184px;">Eligibility</h2>
  <div class="spec" style="left:452px; top:230px;">Borrower</div>
  <div class="val" style="left:606px; top:231px;">Individual or business entity</div>
  <div class="spec" style="left:452px; top:249px;">Eligible property types</div>
  <div class="val" style="left:606px; top:249px; width:200px;">Multifamily Mixed-Use, Retail, Office, Light Industrial, Automotive, Mobile Home Park, Warehouse, Self-Storage, Restaurant/ Bar, Daycare Center</div>
  <div class="val" style="left:606px; top:306px;">No rural properties</div>
  <div class="val" style="left:606px; top:329px; width:205px;">Stabilized properties only (75% occupancy with no rehab or deferred maintenance)</div>
  <div class="spec" style="left:452px; top:367px;">Long-term financing only <span style="font-weight:500;">(no short term/bridge)</span></div>
  <div class="spec" style="left:452px; top:397px;">Eligible states:</div>
  <div class="val" style="left:606px; top:402px; width:200px;">All except ID, HI, MI, MT, ND, NV, SD, VT, WV, WY</div>
  <div class="spec" style="left:452px; top:434px;">Population<br>Requirements</div>
  <div class="val" style="left:606px; top:436px;">Top 300 MSAs</div>

  <h2 class="abs section-title" style="left:57px; top:466px;">General Guidelines</h2>
  <div class="spec" style="left:57px; top:512px;">Loan Size</div>
  <div class="val" style="left:179px; top:511px;">$100,000 - $2 million</div>
  <div class="spec" style="left:57px; top:531px;">Loan Terms</div>
  <div class="val" style="left:179px; top:530px;">30-year fixed | 5-year ARM</div>
  <div class="spec" style="left:57px; top:549px;">Amortization</div>
  <div class="val" style="left:179px; top:548px;">15, 25, 30</div>
  <div class="spec" style="left:57px; top:568px;">Loan Purpose</div>
  <div class="val" style="left:179px; top:567px;">Purchase, Cash-Out, R/T Refi</div>
  <div class="spec" style="left:57px; top:586px;">Max LTV</div>
  <div class="val" style="left:179px; top:585px;">Purchase: 80% | Refi: 75%</div>

  <div class="spec" style="left:435px; top:511px;">Min FICO</div>
  <div class="val" style="left:573px; top:512px;">650</div>
  <div class="spec" style="left:435px; top:530px;">Min DSCR</div>
  <div class="val" style="left:573px; top:531px;">Investor: 1.15x | Owner-Occupied: 1.2x Global</div>
  <div class="spec" style="left:435px; top:549px;">Prepayment<br>Fee Options</div>
  <div class="val" style="left:573px; top:552px; width:225px;">5% for 10, 7, 5, or 3 years 5-year declining (5, 4, 3, 2, 1)</div>
  <div class="spec" style="left:435px; top:584px;">UW Methodology</div>
  <div class="val" style="left:573px; top:586px; width:225px;">Investor: Property DSCR Owner-Occupied: Global DSCR</div>
  <div class="spec" style="left:435px; top:613px;">Buy Downs</div>
  <div class="val" style="left:573px; top:616px;">0.375% = 1 point cost</div>

  <div class="abs matrix">
    <div class="mh"></div>
    <div class="mh">Full Doc</div>
    <div class="mh">Bank Statement</div>
    <div class="mh">Lite Doc</div>
    <div class="mh">No Doc</div>

    <div class="cell row-label">Owner<br>Occupied/Use</div>
    <div class="cell push">
      <div class="yes">Yes,</div>
      <div class="desc">2 Years of Personal &amp; Business Tax Returns must be provided.</div>
      <div class="docs-block">
        <div class="docs-title">Submission Docs:</div>
        <ul class="docs">
          <li>Application</li>
          <li>Credit Report</li>
          <li>If Purchase, Purchase<span class="cont">Contract</span></li>
          <li>Business Debt Schedule</li>
        </ul>
      </div>
    </div>
    <div class="cell">
      <div class="yes">Yes,</div>
      <div class="desc">12 Months of Business Bank Statements must be provided. Therewill be a 70% expense factor attributed to the gross deposits (30% of the income will be used).</div>
      <div class="docs-block" style="margin-top:18px;">
        <div class="docs-title">Submission Docs:</div>
        <ul class="docs">
          <li>Application</li>
          <li>Credit Report</li>
          <li>If Purchase, Purchase<span class="cont">Contract</span></li>
        </ul>
      </div>
    </div>
    <div class="cell"><div class="no">NO</div></div>
    <div class="cell push">
      <div class="yes">Yes,</div>
      <div class="desc">No tax returns or business debt schedule required.</div>
      <div class="docs-block" style="margin-top:auto; margin-bottom:8px;">
        <div class="docs-title">Submission Docs:</div>
        <ul class="docs">
          <li>Application</li>
          <li>Credit Report</li>
          <li>If Purchase,<span class="cont">Purchase</span><span class="cont">Contract</span></li>
        </ul>
      </div>
    </div>

    <div class="cell row-label left last-row">Investment</div>
    <div class="cell last-row">
      <div class="yes">Yes,</div>
      <div class="desc">2 Years of Personal &amp; Business Tax Returns must be provided.</div>
      <div class="docs-block">
        <div class="docs-title">Submission Docs:</div>
        <ul class="docs">
          <li>Application</li>
          <li>Credit Report</li>
          <li>If Purchase, Purchase<span class="cont">Contract</span></li>
          <li>Lease Agreement</li>
          <li>Operating Statement</li>
          <li>Rent Roll</li>
        </ul>
      </div>
    </div>
    <div class="cell last-row"><div class="no">No</div></div>
    <div class="cell last-row">
      <div class="yes">Yes,</div>
      <div class="desc">No tax returns are required for this document type.</div>
      <div class="docs-block">
        <div class="docs-title">Submission Docs:</div>
        <ul class="docs">
          <li>Application</li>
          <li>Credit Report</li>
          <li>If Purchase, Purchase<span class="cont">Contract</span></li>
          <li>Lease Agreement</li>
          <li>Operating Statement</li>
          <li>Rent Roll</li>
        </ul>
      </div>
    </div>
    <div class="cell last-row">
      <div class="yes">Yes,</div>
      <div class="desc">No tax returns, lease agreements, operating state-ments or rent rolls are required.</div>
      <div class="docs-block">
        <div class="docs-title">Submission Docs:</div>
        <ul class="docs">
          <li>Application</li>
          <li>Credit Report</li>
          <li>If Purchase,<span class="cont">Purchase</span><span class="cont">Contract</span></li>
        </ul>
      </div>
    </div>
  </div>
  <div class="abs matrix-frame"></div>

  <svg class="abs footer-band" viewBox="0 0 848 72" aria-hidden="true">
    <path d="M70 72 Q424 0 778 72 Z" fill="var(--grey-band)"/>
    <path d="M34 72 Q424 -6 814 72" fill="none" stroke="var(--ink)" stroke-width="5"/>
  </svg>
  <div class="abs footer-url">WWW.NLCAPITAL.COM</div>

</body>
</html>
```